Business Card for TBQ

We need a Corporate style business card for a new Industrial recycling company based in Australia. We recycle industrial products from Mining companies, power stations and other large industry all around the country.

We want the card to represent a modern, innovative professional company that is an industry leader.

We want the card to be double sided. I think with the logo centred by itself on one side and the text displayed with all our details on the other side.

(or you could put the persons name with the job title on the side with the logo?? I'll leave that up to your creative sides)

Open to how you divide and place the information on the one side of the card.

I think the persons name and the title should have its own place. The rest of the information can be placed as you think is best and then I will provide feedback as to what I think works best.

I have attached the logo file so you can add that to the one side. Whether you use it in a smaller form on the second side too is an option but I'll leave that up to you initially?

Information required on the card is as follows

Darren Holt
Director

0427 318 592

darren@tbqg.com.au

Po Box 782
Corlett ACT 2611

www.tbqg.com.au

ACN 152 876 209 (This can be in very small print and can be in the bottom corner of the card or somewhere not very prominent
Updates

Wanted to thank everyone for their submissions. 

We were really torn on about 5 designs in the end.

We decided to go with the first one we liked.

We have another company that is going to need logo and business card design in the coming weeks.

I will save your designer ID's so I can invite you all to that project. too!

Thanks again and all the best

Darren

Target Market(s)

Corporate and medium to large business clients

Industry/Entity Type

Industrial

```html
<!DOCTYPE html>
<html lang="en">
<head>
<meta charset="utf-8">
<title>TBQ Group — Business Card</title>
<link rel="stylesheet" href="https://fonts.googleapis.com/css2?family=Michroma&family=Open+Sans:wght@400;700&display=swap">
<style>
  :root {
    --bg: #e4e4e4;
    --paper: #ffffff;
    --green: #9cc93a;
    --green-light: #b4d84f;
    --green-pale: #c9e38a;
    --green-deep: #3f9b35;
    --blue: #3d86c6;
    --ink: #2b2b2b;
    --white: #ffffff;
  }
  * { margin: 0; padding: 0; box-sizing: border-box; }
  html, body {
    width: 1200px; height: 1000px; overflow: hidden;
    background: var(--bg);
  }
  .sheet {
    position: relative; width: 1200px; height: 1000px;
  }
  .card {
    position: absolute; left: 260px; width: 680px; height: 416px;
    background: var(--paper);
    box-shadow: 0 6px 18px rgba(0,0,0,0.12);
    overflow: hidden;
  }
  .card--front { top: 48px; }
  .card--back { top: 520px; }

  .brand {
    position: absolute; display: flex; align-items: center; gap: 14px;
  }
  .brand__dot {
    width: 42px; height: 42px; border-radius: 50%; background: var(--green-deep);
  }
  .brand__name {
    font-family: "Michroma", sans-serif; font-size: 26px;
    color: var(--ink); letter-spacing: 1px;
  }
  .card--front .brand { left: 50%; top: 50%; transform: translate(-50%, -50%); }
  .card--back .brand { left: 90px; top: 262px; }
  .card--back .brand__dot { width: 34px; height: 34px; }
  .card--back .brand__name { font-size: 22px; }

  .back__art { position: absolute; inset: 0; }

  .acn {
    position: absolute; top: 16px; right: 20px;
    font-family: "Open Sans", sans-serif; font-size: 9px; color: var(--white);
  }
  .contact {
    position: absolute; left: 420px; top: 86px; width: 230px;
    color: var(--white); font-family: "Open Sans", sans-serif;
  }
  .contact__name {
    font-family: "Michroma", sans-serif; font-size: 19px; letter-spacing: 1px;
    text-transform: uppercase; line-height: 1.1;
  }
  .contact__title {
    font-family: "Michroma", sans-serif; font-size: 10px; letter-spacing: 1px;
    text-transform: uppercase; margin-top: 4px; padding-bottom: 8px;
    border-bottom: 1px solid var(--white);
  }
  .contact__list { margin-top: 12px; font-size: 11px; line-height: 1.35; }
  .contact__label { font-weight: 700; }
  .contact__value { padding-left: 14px; }
  .contact__web { margin-top: 14px; font-size: 11px; font-weight: 700; }
</style>
</head>
<body>
<main class="sheet">
  <section class="card card--front" aria-label="Card front">
    <div class="brand">
      <span class="brand__dot"></span>
      <span class="brand__name">TBQ Group</span>
    </div>
  </section>

  <section class="card card--back" aria-label="Card back">
    <svg class="back__art" viewBox="0 0 680 416" width="680" height="416" aria-hidden="true">
      <defs>
        <linearGradient id="greenField" x1="0" y1="0" x2="1" y2="1">
          <stop offset="0" stop-color="#8cc23a"/>
          <stop offset="1" stop-color="#abd23c"/>
        </linearGradient>
      </defs>
      <rect width="680" height="416" fill="url(#greenField)"/>
      <path d="M0,96 C200,70 400,170 470,416 L0,416 Z" fill="var(--green-pale)" opacity="0.6"/>
      <path d="M0,116 C200,92 390,185 455,416 L0,416 Z" fill="var(--green-light)"/>
      <path d="M0,136 C200,112 378,200 440,416 L0,416 Z" fill="var(--green-pale)"/>
      <path d="M0,152 C200,130 368,212 430,416 L0,416 Z" fill="var(--blue)"/>
      <path d="M0,160 C200,140 360,220 422,416 L0,416 Z" fill="var(--paper)"/>
    </svg>

    <div class="acn">ACN 152 876 209</div>

    <div class="contact">
      <h1 class="contact__name">Darren Holt</h1>
      <p class="contact__title">Director</p>
      <dl class="contact__list">
        <dt class="contact__label">Phone</dt>
        <dd class="contact__value">0427 318 592</dd>
        <dt class="contact__label">Email</dt>
        <dd class="contact__value">darren@tbqg.com.au</dd>
        <dt class="contact__label">Address</dt>
        <dd class="contact__value">Po Box 782<br>Corlett ACT 2611</dd>
      </dl>
      <p class="contact__web">www.tbqg.com.au</p>
    </div>

    <div class="brand">
      <span class="brand__dot"></span>
      <span class="brand__name">TBQ Group</span>
    </div>
  </section>
</main>
</body>
</html>
```